Business card/Stationary for mobile ultrasound company
Corvin Ultrasound Services, LLC
Business card/Stationary for mobile ultrasound company -
Creative Brief
Use specific fonts
can use a combination of fonts similar to logo
Professional
Tessa Quillon RDMS, RVT, RCS
Owner
P.O. Box 482 Brightwater, NM 87999-0482
4quillons@mailnest.example
I am currently getting a website designed so i will add a web address and an updated email address specifically for the business. I am torn as to use a one sided or 2 sided card. So im open. I would rather not have the address on the card. Thanks
Innovative mobile technology focused on improving the QUALITY of patient care. (The wording can change but along this idea)

```html
<!DOCTYPE html>
<html lang="en">
<head>
<meta charset="utf-8">
<title>Corvin Ultrasound Services – Business Card</title>
<link href="https://fonts.googleapis.com/css2?family=PT+Sans:ital,wght@0,400;0,700;1,400;1,700&display=swap" rel="stylesheet">
<style>
  :root {
    --page-bg: #d9d9d9;
    --card-black: #0b0b0b;
    --olive: #7d7a4a;
    --paper-white: #ffffff;
    --text-white: #f4f4f4;
    --text-soft: #c9c9c9;
    --divider: #6a6a6a;
  }
  html, body {
    margin: 0;
    padding: 0;
    width: 1200px;
    height: 780px;
    overflow: hidden;
    background: var(--page-bg);
  }
  .canvas {
    position: relative;
    width: 1200px;
    height: 780px;
  }
  .card {
    position: absolute;
    left: 75px;
    top: 90px;
    width: 1050px;
    height: 600px;
    border-radius: 34px;
    overflow: hidden;
    background: var(--card-black);
    font-family: "PT Sans", Arial, sans-serif;
    color: var(--text-white);
  }
  .card-wave {
    position: absolute;
    inset: 0;
    width: 100%;
    height: 100%;
  }
  .brand {
    position: absolute;
    left: 60px;
    top: 185px;
    width: 470px;
    text-align: center;
    color: var(--text-white);
    font-weight: 400;
  }
  .brand-name {
    display: block;
    font-size: 92px;
    line-height: 1;
    letter-spacing: 1px;
  }
  .brand-tagline {
    display: block;
    font-size: 27px;
    margin-top: 6px;
  }
  .divider {
    position: absolute;
    left: 563px;
    top: 80px;
    width: 2px;
    height: 250px;
    background: var(--divider);
  }
  .contact {
    position: absolute;
    left: 600px;
    top: 80px;
  }
  .contact-name {
    margin: 0;
    font-size: 26px;
    font-weight: 700;
    font-style: italic;
    line-height: 1.2;
  }
  .contact-role {
    margin: 4px 0 0;
    font-size: 23px;
    line-height: 1.2;
  }
  .contact-address {
    margin: 62px 0 0;
    font-size: 20px;
    line-height: 1.35;
    color: var(--text-soft);
    font-style: normal;
  }
  .contact-line {
    display: flex;
    align-items: center;
    gap: 12px;
    font-size: 20px;
    color: var(--text-soft);
    margin-top: 14px;
  }
  .contact-line svg {
    width: 20px;
    height: 20px;
    flex: none;
  }
  .contact-line.first { margin-top: 22px; }
</style>
</head>
<body>
<main class="canvas">
  <section class="card" aria-label="Business card">
    <svg class="card-wave" viewBox="0 0 1050 600" preserveAspectRatio="none" aria-hidden="true">
      <path d="M0,548 C300,520 640,480 820,430 C920,402 1000,370 1050,340 L1050,372 C960,440 760,520 0,572 Z" fill="var(--olive)"/>
      <path d="M0,600 L0,582 C420,560 800,500 1050,386 L1050,600 Z" fill="var(--paper-white)"/>
    </svg>

    <div class="brand">
      <span class="brand-name">Corvin</span>
      <span class="brand-tagline">Ultrasound Services, LLC</span>
    </div>

    <div class="divider"></div>

    <div class="contact">
      <p class="contact-name">Tessa Quillon RDMS, RVT, RCS</p>
      <p class="contact-role">Owner</p>
      <address class="contact-address">P.O. Box 482<br>Brightwater, NM 87999-0482</address>
      <div class="contact-line first">
        <svg viewBox="0 0 24 24" aria-label="Phone"><path fill="#f4f4f4" d="M6.6 10.8c1.4 2.8 3.8 5.2 6.6 6.6l2.2-2.2c.3-.3.7-.4 1-.2 1.1.4 2.3.6 3.6.6.6 0 1 .4 1 1V20c0 .6-.4 1-1 1C10.6 21 3 13.4 3 4c0-.6.4-1 1-1h3.5c.6 0 1 .4 1 1 0 1.3.2 2.5.6 3.6.1.3 0 .7-.2 1z"/></svg>
        <span>575-555-0148</span>
      </div>
      <div class="contact-line">
        <svg viewBox="0 0 24 24" aria-label="Email"><text x="12" y="19" text-anchor="middle" font-family="PT Sans, Arial, sans-serif" font-size="21" font-weight="700" fill="#f4f4f4">@</text></svg>
        <span>4quillons@mailnest.example</span>
      </div>
    </div>
  </section>
</main>
</body>
</html>
```